Home loan promotion flyer (DL or Postcard)

We need a flyer that promotes our home loan broking service. In summary, we are an Australian financial planning business that helps Gen X and Y make better financial planning decisions.

We would like the design to have a similar look and feel to the following:
http://www.leaflet-vault.com.au/qmpr/bright_path_steady_living/

Text that I would like included is:

(HEADING) Awesome Debt Management: Someone else's money used to Your advantage.

(Paragraph) Debt is not necessarily a dirty work. Smart Australian investors often use debt strategies to minimise tax burdens, pay off their home loan sooner and to build their wealth quicker.

(Promotion) Bring this along to your COMPLIMENTARY finance health check and we will give you a $25 Durban Vale voucher to celebrate your first step towards a better financial future. (Please include the image of the voucher near this text).

Finally, you must include our number (1300 614 972) and website (www.qmpr.com.au)

Apart from being consistent with the e-brochure above (please ensure you view the link), we would like the design to be bold and stand out from the crowd.

I have attached a previous home loan promotion design that I like but I feel that there are too many words and not enough space. Please use the good elements but avoid the rest.

Finally, I've also attached a DL "goldfish" design that I really like because I think the design is memorable and stands-out.
Updates

Reason: Hi there designers Thanks for your designs so far. They look great. I have extended the brief to give everyone the opportunity to reassess their design to make sure that it is consistent with the design brief. If anything is unclear please don't hesitate to make contact. Thanks TR

Target Market(s)

Australian first home buyers and property investors.

Industry/Entity Type

Financial

Requirements
Must have
• The design MUST be consistent with the existing marketing material referred to in this link.

```html
<!DOCTYPE html>
<html lang="en">
<head>
<meta charset="utf-8">
<title>Awesome Debt Management – Flyer</title>
<link rel="stylesheet" href="https://fonts.googleapis.com/css2?family=Arimo:wght@400;700&display=swap">
<style>
  :root {
    --green: #72b84f;
    --green-text: #8cc63f;
    --black: #000000;
    --white: #ffffff;
  }
  * { margin: 0; padding: 0; box-sizing: border-box; }
  html, body { width: 1200px; height: 2523px; overflow: hidden; background: var(--black); }
  .flyer {
    position: relative; width: 1200px; height: 2523px; overflow: hidden;
    background: var(--black); font-family: "Arimo", Arial, sans-serif;
  }
  .header-band {
    position: absolute; left: 0; top: 0; width: 1200px; height: 984px;
    background: var(--green);
  }
  .quote-mark {
    position: absolute; font-weight: 700; font-size: 230px; line-height: 1;
    color: var(--black);
  }
  .quote-open { left: 28px; top: 6px; }
  .quote-close { left: 1092px; top: 704px; }
  .rule {
    position: absolute; left: 42px; height: 7px; background: var(--white);
  }
  .rule-top { top: 136px; width: 1124px; }
  .rule-bottom { top: 698px; width: 1052px; }
  .headline {
    position: absolute; left: 42px; top: 146px; width: 1150px;
    font-weight: 700; font-size: 130px; line-height: 112px;
    color: var(--black); text-transform: uppercase; white-space: nowrap;
  }
  .subhead {
    position: absolute; left: 42px; top: 448px; width: 1150px;
    font-weight: 400; font-size: 99px; line-height: 118px; color: var(--white);
    white-space: nowrap;
  }
  .contact {
    position: absolute; left: 42px; top: 800px;
    font-weight: 700; font-size: 56px; line-height: 74px; color: var(--white);
  }
  .intro {
    position: absolute; left: 42px; top: 1008px; width: 1140px;
    font-size: 60px; line-height: 72px; color: var(--green-text); white-space: nowrap;
  }
  .offer {
    position: absolute; left: 60px; top: 1540px;
    font-size: 70px; line-height: 79px; color: var(--white); white-space: nowrap;
  }
  .voucher-visual { position: absolute; left: 600px; top: 1480px; width: 600px; height: 1043px; }
</style>
</head>
<body>
<main class="flyer">
  <section class="header-band">
    <span class="quote-mark quote-open">&ldquo;</span>
    <div class="rule rule-top"></div>
    <h1 class="headline">Awesome Debt<br>Management:</h1>
    <p class="subhead">Someone else’s money<br>used to Your advantage</p>
    <div class="rule rule-bottom"></div>
    <span class="quote-mark quote-close">&rdquo;</span>
    <p class="contact">1300 614 972<br>www.qmpr.com.au</p>
  </section>

  <p class="intro">Debt is not necessarily a dirty work.<br>Smart Australian investors often<br>use debt strategies to minimise tax<br>burdens, pay off their home loan<br>sooner and to build their wealth quicker.</p>

  <svg class="voucher-visual" viewBox="0 0 600 1043" role="img" aria-label="Gift card in a silver ribbon-wrapped box above stacks of gold coins">
    <defs>
      <radialGradient id="giftGlow" cx="50%" cy="50%" r="50%">
        <stop offset="0%" stop-color="#ffffff"/>
        <stop offset="75%" stop-color="#e4e4e4"/>
        <stop offset="100%" stop-color="#9a9a9a"/>
      </radialGradient>
      <linearGradient id="coinTone" x1="0" y1="0" x2="0" y2="1">
        <stop offset="0%" stop-color="#b78a3e"/>
        <stop offset="100%" stop-color="#5a3d18"/>
      </linearGradient>
    </defs>
    <circle cx="426" cy="322" r="297" fill="url(#giftGlow)"/>
    <rect x="6" y="479" width="594" height="564" fill="url(#coinTone)"/>
  </svg>

  <p class="offer">Bring this along to your<br>COMPLIMENTARY<br>finance health<br>check and we will<br>give you a $25<br>Durban Vale<br>voucher to<br>celebrate<br>your first<br>step towards<br>a better<br>financial future.</p>
</main>
</body>
</html>
```